Stationery Design Project

Please create a custom stationery set for Heron Financial. The logo is attached to this brief.

Industry/Entity Type

Financial

```html
<!DOCTYPE html>
<html lang="en">
<head>
<meta charset="utf-8">
<title>Heron Financial – Stationery Set</title>
<link rel="stylesheet" href="https://fonts.googleapis.com/css2?family=Cinzel:wght@400;600&display=swap">
<style>
  :root {
    --navy: #33366e;
    --ink: #2b2b2b;
    --paper-light: #e6e6e6;
    --paper-mid: #d9d9d9;
    --paper-dark: #cfcfcf;
    --page: #ffffff;
  }
  * { margin: 0; padding: 0; box-sizing: border-box; }
  html, body {
    width: 1200px; height: 2369px; overflow: hidden;
    background: var(--page);
    font-family: "Cinzel", "Times New Roman", serif;
    color: var(--ink);
  }
  .canvas { position: relative; width: 1200px; height: 2369px; }

  .sheet { position: absolute; overflow: hidden; }
  .sheet__texture {
    position: absolute; inset: 0;
    background:
      linear-gradient(180deg, rgba(255,255,255,0.35), rgba(255,255,255,0) 40%, rgba(0,0,0,0.03) 70%, rgba(255,255,255,0.2)),
      linear-gradient(135deg, var(--paper-light), var(--paper-mid) 55%, var(--paper-dark));
  }
  .paw { position: absolute; background: var(--navy); }
  .paw--top-left { top: 0; left: 0; border-bottom-right-radius: 100%; }
  .paw--bottom-right { right: 0; bottom: 0; border-top-left-radius: 100%; }

  .brand { position: absolute; text-align: center; color: var(--navy); font-weight: 400; line-height: 1; }
  .brand__name { display: block; letter-spacing: 0.12em; }
  .brand__sub { display: block; letter-spacing: 0.55em; margin-right: -0.55em; }

  .contact { position: absolute; }
  .contact__corner {
    position: absolute; border-top: 4px solid var(--navy); border-left: 4px solid var(--navy);
  }
  .contact__list { display: grid; grid-template-columns: auto 1fr; text-transform: uppercase; }
  .contact__label { color: var(--navy); }
  .contact__value { color: var(--ink); }
  .contact__abn { text-transform: uppercase; color: var(--ink); }

  /* Letterhead */
  .letterhead { left: 84px; top: 78px; width: 1020px; height: 1457px; }
  .letterhead .paw--top-left { width: 172px; height: 172px; }
  .letterhead .paw--bottom-right { width: 170px; height: 178px; }
  .letterhead .brand { right: 58px; top: 150px; width: 205px; }
  .letterhead .brand__name { font-size: 44px; }
  .letterhead .brand__sub { font-size: 14px; margin-top: 10px; }
  .letterhead .contact { left: 53px; top: 1172px; font-size: 19px; }
  .letterhead .contact__corner { left: 0; top: 0; width: 16px; height: 20px; }
  .letterhead .contact__list { margin-left: 24px; padding-top: 6px; line-height: 24.5px; column-gap: 10px; }
  .letterhead .contact__abn { margin-left: 132px; margin-top: 24px; }

  /* Compliment slip */
  .slip { left: 84px; top: 1558px; width: 1020px; height: 486px; }
  .slip .paw--top-left { width: 122px; height: 130px; }
  .slip .paw--bottom-right { width: 120px; height: 146px; }
  .slip .brand { right: 29px; top: 150px; width: 200px; }
  .slip .brand__name { font-size: 44px; }
  .slip .brand__sub { font-size: 14px; margin-top: 10px; }
  .slip .contact { left: 26px; top: 264px; font-size: 18px; }
  .slip .contact__corner { left: 0; top: 0; width: 15px; height: 19px; }
  .slip .contact__list { margin-left: 20px; padding-top: 6px; line-height: 24px; column-gap: 10px; }
  .slip .contact__abn { margin-left: 89px; margin-top: 18px; }

  /* Standalone mark */
  .brand--standalone { left: 154px; top: 2238px; width: 257px; }
  .brand--standalone .brand__name { font-size: 60px; }
  .brand--standalone .brand__sub { font-size: 21px; margin-top: 10px; }

  /* Business card */
  .card { left: 672px; top: 2070px; width: 432px; height: 249px; }
  .card .paw--top-left { width: 57px; height: 59px; }
  .card .paw--bottom-right { width: 58px; height: 64px; }
  .card .brand { right: 12px; top: 50px; width: 80px; }
  .card .brand__name { font-size: 16px; }
  .card .brand__sub { font-size: 5.5px; margin-top: 4px; }
  .card .contact { left: 17px; top: 126px; font-size: 8.5px; }
  .card .contact__corner { left: 0; top: 0; width: 7px; height: 9px; border-width: 2px; }
  .card .contact__list { margin-left: 9px; padding-top: 3px; line-height: 10.7px; column-gap: 6px; }
  .card .contact__abn { margin-left: 60px; margin-top: 10px; }
</style>
</head>
<body>
<main class="canvas">

  <section class="sheet letterhead" aria-label="Letterhead">
    <div class="sheet__texture" role="img" aria-label="Pale grey woodgrain paper texture"></div>
    <div class="paw paw--top-left" role="img" aria-label="Navy paw print decoration"></div>
    <div class="paw paw--bottom-right" role="img" aria-label="Navy paw print decoration"></div>
    <div class="brand"><span class="brand__name">Heron</span><span class="brand__sub">Financial</span></div>
    <div class="contact">
      <span class="contact__corner"></span>
      <dl class="contact__list">
        <dt class="contact__label">Address:</dt><dd class="contact__value">Suite 14</dd>
        <dt></dt><dd class="contact__value">48 Wattle St</dd>
        <dt></dt><dd class="contact__value">Melbourne VIC 3000</dd>
        <dt class="contact__label">Phone:</dt><dd class="contact__value">03 9000 4180</dd>
        <dt class="contact__label">Fax:</dt><dd class="contact__value">03 9000 4181</dd>
        <dt class="contact__label">Email:</dt><dd class="contact__value">info@heronfinancial.com.au</dd>
        <dt class="contact__label">Website:</dt><dd class="contact__value">www.heronfinancial.com.au</dd>
      </dl>
      <p class="contact__abn">ABN 12 345 678 901</p>
    </div>
  </section>

  <section class="sheet slip" aria-label="Compliment slip">
    <div class="sheet__texture" role="img" aria-label="Pale grey woodgrain paper texture"></div>
    <div class="paw paw--top-left" role="img" aria-label="Navy paw print decoration"></div>
    <div class="paw paw--bottom-right" role="img" aria-label="Navy paw print decoration"></div>
    <div class="brand"><span class="brand__name">Heron</span><span class="brand__sub">Financial</span></div>
    <div class="contact">
      <span class="contact__corner"></span>
      <dl class="contact__list">
        <dt class="contact__label">Address:</dt><dd class="contact__value">Suite 14</dd>
        <dt></dt><dd class="contact__value">48 Wattle St</dd>
        <dt></dt><dd class="contact__value">Melbourne VIC 3000</dd>
        <dt class="contact__label">Phone:</dt><dd class="contact__value">03 9000 4180</dd>
        <dt class="contact__label">Fax:</dt><dd class="contact__value">03 9000 4181</dd>
        <dt class="contact__label">Email:</dt><dd class="contact__value">info@heronfinancial.com.au</dd>
        <dt class="contact__label">Website:</dt><dd class="contact__value">www.heronfinancial.com.au</dd>
      </dl>
      <p class="contact__abn">ABN 12 345 678 901</p>
    </div>
  </section>

  <div class="brand brand--standalone"><span class="brand__name">Heron</span><span class="brand__sub">Financial</span></div>

  <section class="sheet card" aria-label="Business card">
    <div class="sheet__texture" role="img" aria-label="Pale grey woodgrain paper texture"></div>
    <div class="paw paw--top-left" role="img" aria-label="Navy paw print decoration"></div>
    <div class="paw paw--bottom-right" role="img" aria-label="Navy paw print decoration"></div>
    <div class="brand"><span class="brand__name">Heron</span><span class="brand__sub">Financial</span></div>
    <div class="contact">
      <span class="contact__corner"></span>
      <dl class="contact__list">
        <dt class="contact__label">Address:</dt><dd class="contact__value">Suite 14</dd>
        <dt></dt><dd class="contact__value">48 Wattle St</dd>
        <dt></dt><dd class="contact__value">Melbourne VIC 3000</dd>
        <dt class="contact__label">Phone:</dt><dd class="contact__value">03 9000 4180</dd>
        <dt class="contact__label">Fax:</dt><dd class="contact__value">03 9000 4181</dd>
        <dt class="contact__label">Email:</dt><dd class="contact__value">info@heronfinancial.com.au</dd>
        <dt class="contact__label">Website:</dt><dd class="contact__value">www.heronfinancial.com.au</dd>
      </dl>
      <p class="contact__abn">ABN 12 345 678 901</p>
    </div>
  </section>

</main>
</body>
</html>
```